Stationary Design

Harbor Stagecraft Collective, Inc
27410 Marlowe Blvd Ste 4, Larkspur Flats, OR 90512
Office: 555-584-2760 Email: admin@hsccrew.example

Industry/Entity Type

Entertainment

Colors
0054AA
0677BA
7BADD7
CADEEF
E8F1F8

```html
<!DOCTYPE html>
<html lang="en">
<head>
<meta charset="utf-8">
<title>Harbor Stagecraft Collective — Business Card</title>
<link rel="stylesheet" href="https://fonts.googleapis.com/css2?family=Montserrat:wght@400;500;600;700;800&display=swap">
<style>
  :root {
    --brand-blue: #0054AA;
    --brand-blue-mid: #0677BA;
    --brand-blue-soft: #7BADD7;
    --brand-blue-pale: #CADEEF;
    --brand-blue-mist: #E8F1F8;
    --ink: #1d1d1f;
    --stage: #232323;
    --card-white: #ffffff;
    --night-deep: #0d1a4a;
    --night-mid: #1f3f8c;
  }
  * { box-sizing: border-box; margin: 0; padding: 0; }
  html, body { width: 1200px; height: 711px; overflow: hidden; }
  body {
    background: var(--stage);
    font-family: "Montserrat", sans-serif;
    position: relative;
  }
  .card {
    position: absolute;
    top: 96px;
    width: 300px;
    height: 520px;
    border-radius: 22px;
    overflow: hidden;
  }
  /* Front */
  .card--front {
    left: 270px;
    background: linear-gradient(180deg, var(--night-deep) 0%, var(--night-mid) 100%);
  }
  .front-brand {
    position: absolute;
    top: 46px; left: 0; right: 0;
    display: flex; flex-direction: column; align-items: center; gap: 12px;
  }
  .brand-dot {
    width: 46px; height: 46px; border-radius: 50%;
    background: var(--brand-blue-mid);
  }
  .front-brand .brand-name {
    color: var(--brand-blue-pale);
    font-weight: 700; font-size: 13px; letter-spacing: .08em;
    text-transform: uppercase; text-align: center; line-height: 1.4;
  }
  .city-photo {
    position: absolute; left: 0; right: 0; bottom: 0; height: 340px;
    background: linear-gradient(180deg, #1c2f74 0%, #2d4fa8 35%, #35467a 60%, #1a2240 100%);
  }
  /* Back */
  .card--back {
    left: 630px;
    background: var(--card-white);
    text-align: center;
  }
  .back-brand {
    margin-top: 44px;
    display: flex; flex-direction: column; align-items: center; gap: 12px;
  }
  .back-brand .brand-dot { width: 58px; height: 58px; background: var(--brand-blue); }
  .back-brand .brand-name {
    color: var(--brand-blue);
    font-weight: 700; font-size: 15px; letter-spacing: .06em;
    text-transform: uppercase; line-height: 1.35;
  }
  .brand-rule {
    width: 200px; height: 2px; background: var(--brand-blue); margin: 10px auto 0;
  }
  .person { margin-top: 34px; }
  .person-name {
    color: var(--brand-blue); font-weight: 800; font-size: 20px; letter-spacing: .02em;
  }
  .person-title { color: var(--ink); font-size: 12px; font-weight: 500; margin-top: 2px; }
  .dot-row { display: block; margin: 16px auto 0; }
  .contact-list { list-style: none; margin-top: 10px; }
  .contact-list li { color: var(--ink); font-size: 12.5px; font-weight: 500; line-height: 1.55; }
  .address { margin-top: 8px; font-style: normal; }
  .address .company { color: var(--brand-blue); font-weight: 600; }
  .address span { display: block; color: var(--ink); font-size: 12.5px; font-weight: 500; line-height: 1.55; }
  .address span.company { color: var(--brand-blue); font-weight: 600; }
</style>
</head>
<body>

<section class="card card--front" aria-label="Card front">
  <div class="front-brand">
    <span class="brand-dot"></span>
    <p class="brand-name">Harbor Stagecraft<br>Collective</p>
  </div>
  <div class="city-photo" role="img" aria-label="Night city skyline photograph with lit towers"></div>
</section>

<section class="card card--back" aria-label="Card back">
  <div class="back-brand">
    <span class="brand-dot"></span>
    <p class="brand-name">Harbor Stagecraft<br>Collective</p>
  </div>
  <div class="brand-rule"></div>

  <div class="person">
    <h1 class="person-name">MARCUS ELLERY</h1>
    <p class="person-title">Managing Director</p>
  </div>

  <svg class="dot-row" width="260" height="26" viewBox="0 0 260 26" aria-hidden="true">
    <g fill="var(--brand-blue)">
      <circle cx="3" cy="13" r="2.5"/><circle cx="14" cy="13" r="3.5"/><circle cx="27" cy="13" r="4.5"/>
      <circle cx="42" cy="13" r="5.5"/><circle cx="60" cy="13" r="6.5"/><circle cx="80" cy="13" r="7"/>
      <circle cx="104" cy="13" r="11"/><circle cx="130" cy="13" r="11"/><circle cx="156" cy="13" r="11"/>
      <circle cx="180" cy="13" r="7"/><circle cx="200" cy="13" r="6.5"/><circle cx="218" cy="13" r="5.5"/>
      <circle cx="233" cy="13" r="4.5"/><circle cx="246" cy="13" r="3.5"/><circle cx="257" cy="13" r="2.5"/>
    </g>
    <path d="M99 10 q0 -2 2 -2 l2 0 l1 3 l-1.5 1 q1.5 3 4 4 l1 -1.5 l3 1 l0 2 q0 2 -2 2 q-9 -1 -9.5 -9.5z" fill="#fff"/>
    <g fill="none" stroke="#fff" stroke-width="1.4" stroke-linecap="round">
      <rect x="124" y="9" width="12" height="8" rx="1"/><path d="M124 9 l6 5 l6 -5"/>
      <circle cx="156" cy="13" r="6"/><path d="M150 13 h12 M156 7 q-3 6 0 12 M156 7 q3 6 0 12"/>
    </g>
  </svg>

  <ul class="contact-list">
    <li>555-584-2760</li>
    <li>admin@hsccrew.example</li>
    <li>www.hsccrew.site</li>
  </ul>

  <svg class="dot-row" width="260" height="26" viewBox="0 0 260 26" aria-hidden="true">
    <g fill="var(--brand-blue)">
      <circle cx="3" cy="13" r="2.5"/><circle cx="14" cy="13" r="3.5"/><circle cx="27" cy="13" r="4.5"/>
      <circle cx="42" cy="13" r="5.5"/><circle cx="60" cy="13" r="6.5"/><circle cx="80" cy="13" r="7"/>
      <circle cx="104" cy="13" r="8.5"/><circle cx="130" cy="13" r="11"/><circle cx="156" cy="13" r="8.5"/>
      <circle cx="180" cy="13" r="7"/><circle cx="200" cy="13" r="6.5"/><circle cx="218" cy="13" r="5.5"/>
      <circle cx="233" cy="13" r="4.5"/><circle cx="246" cy="13" r="3.5"/><circle cx="257" cy="13" r="2.5"/>
    </g>
    <path d="M130 20 l-4.5 -6 a5 5 0 1 1 9 0 z" fill="none" stroke="#fff" stroke-width="1.4" stroke-linejoin="round"/>
    <circle cx="130" cy="11.5" r="1.6" fill="#fff"/>
  </svg>

  <address class="address">
    <span class="company">Harbor Stagecraft Collective, Inc</span>
    <span>27410 Marlowe Blvd Ste 4,</span>
    <span>Larkspur Flats, OR 90512</span>
  </address>
</section>

</body>
</html>
```